Business card and stationnary for a doctor specialized in Orthopedic Surgery
Dr. Lucien R. Desrosiers
Business card and stationnary for a doctor specialized in Orthopedic Surgery - Medical
Creative Brief
Professional
Chirurgie Orthopédique
DO NOT LIST ADDRESS!
lucien@drdesrosiers-ortho.example
www.drdesrosiers-ortho.example
Concerning the business card, which matters most, please take into consideration the following: 1/ I need my name to be followed below it by my specialty and credentials, each on a separate line as follows Dr. Lucien R. Desrosiers Chirurgie Orthopédique Diplômé de l'UBK et l'Univ de Morvanne Ancien Interne des Hôpitaux de Clervaux 2/ I do not want any address to be listed 3/ my logo can be used either in the front but in a disrete way, or on the back as a watermark or in a corner....i will see which design is more clean and professional. 4/ Concerning the back of the business card, i need please TWO variations: - one without any text on the back except perhaps the logo or website, as u wish -and another one where you provide a place i can input four addresses myself later on ( you can write for now Hospital 1, address, tel...Hospital 2, address, tel , etc.. and i will edit them myself later on)

```html
<!DOCTYPE html>
<html lang="fr">
<head>
<meta charset="utf-8">
<title>Dr. Lucien R. Desrosiers — Cartes de visite</title>
<link href="https://fonts.googleapis.com/css2?family=Tinos:wght@400;700&display=swap" rel="stylesheet">
<style>
  :root {
    --bg: #1c1c1e;
    --card-white: #ffffff;
    --card-silver: #dcdde0;
    --blue-deep: #0b3f8c;
    --blue-mid: #1d63c4;
    --blue-light: #3f8fe6;
    --stripe-grey: #b9bcc2;
    --text-blue: #1a4f9e;
    --text-light: #ffffff;
  }
  * { box-sizing: border-box; margin: 0; padding: 0; }
  html, body { width: 1200px; height: 901px; overflow: hidden; }
  body {
    background: var(--bg);
    font-family: "Tinos", "Times New Roman", serif;
    position: relative;
  }
  .card {
    position: absolute;
    width: 560px;
    height: 320px;
    border-radius: 22px;
    overflow: hidden;
    background: linear-gradient(135deg, var(--card-white) 0%, #f3f4f6 55%, var(--card-silver) 100%);
  }
  .card--back { left: 320px; top: 100px; }
  .card--front { left: 320px; top: 481px; }

  .brand-name {
    font-family: "Tinos", "Times New Roman", serif;
    font-weight: 700;
    color: var(--blue-mid);
    letter-spacing: 1px;
  }
  .card--back .brand {
    position: absolute;
    left: 0; right: 0; top: 118px;
    text-align: center;
  }
  .card--back .brand-name { font-size: 40px; }
  .card--back .website {
    position: absolute;
    left: 0; right: 0; top: 186px;
    text-align: center;
    font-size: 13px;
    color: var(--text-blue);
    letter-spacing: 0.5px;
  }

  .card--front .wave { position: absolute; inset: 0; }
  .card--front .brand {
    position: absolute;
    left: 34px; top: 58px;
  }
  .card--front .brand-name { font-size: 30px; }

  .details {
    position: absolute;
    right: 30px;
    top: 34px;
    text-align: right;
    color: var(--text-light);
  }
  .details .name { font-size: 17px; font-weight: 700; margin-bottom: 4px; }
  .details .credential { font-size: 11.5px; line-height: 1.35; }
  .contacts { margin-top: 26px; }
  .contact {
    display: flex;
    justify-content: flex-end;
    align-items: center;
    gap: 8px;
    font-size: 11.5px;
    line-height: 1.9;
  }
  .contact svg { width: 10px; height: 10px; flex: none; }
</style>
</head>
<body>

  <section class="card card--back" aria-label="Verso de la carte">
    <div class="brand"><span class="brand-name">Desrosiers Ortho</span></div>
    <p class="website">www.drdesrosiers-ortho.example</p>
  </section>

  <section class="card card--front" aria-label="Recto de la carte">
    <svg class="wave" viewBox="0 0 560 320" preserveAspectRatio="none" aria-hidden="true">
      <defs>
        <linearGradient id="blueBand" x1="0" y1="1" x2="1" y2="0">
          <stop offset="0" stop-color="var(--blue-light)"/>
          <stop offset="0.5" stop-color="var(--blue-mid)"/>
          <stop offset="1" stop-color="var(--blue-deep)"/>
        </linearGradient>
      </defs>
      <path d="M268,0 C350,0 330,150 200,208 C130,240 60,252 0,258 L0,320 L560,320 L560,0 Z" fill="var(--stripe-grey)"/>
      <path d="M290,0 C372,0 352,160 220,220 C145,252 70,264 0,270 L0,320 L560,320 L560,0 Z" fill="url(#blueBand)"/>
    </svg>

    <div class="brand"><span class="brand-name">Desrosiers Ortho</span></div>

    <div class="details">
      <p class="name">Dr. Lucien R. Desrosiers</p>
      <p class="credential">Chirurgie Orthopédique</p>
      <p class="credential">Diplômé de l'UBK et l'Univ de Morvanne</p>
      <p class="credential">Ancien Interne des Hôpitaux de Clervaux</p>

      <div class="contacts">
        <p class="contact">(+000) -3- 555 014
          <svg viewBox="0 0 10 10"><rect x="2.5" y="0.5" width="5" height="9" rx="1" fill="none" stroke="#fff" stroke-width="1"/></svg>
        </p>
        <p class="contact">lucien@drdesrosiers-ortho.example
          <svg viewBox="0 0 10 10"><rect x="0.5" y="2" width="9" height="6" fill="none" stroke="#fff" stroke-width="1"/><path d="M0.5,2 L5,5.5 L9.5,2" fill="none" stroke="#fff" stroke-width="1"/></svg>
        </p>
        <p class="contact">www.drdesrosiers-ortho.example
          <svg viewBox="0 0 10 10"><circle cx="5" cy="5" r="4.3" fill="none" stroke="#fff" stroke-width="1"/><path d="M0.7,5 H9.3 M5,0.7 C2.5,3 2.5,7 5,9.3 M5,0.7 C7.5,3 7.5,7 5,9.3" fill="none" stroke="#fff" stroke-width="0.8"/></svg>
        </p>
      </div>
    </div>
  </section>

</body>
</html>
```